Talvero Engineering & Management Services Website

A professional website design that outlines Engineering and Management Services. The website is to be colour coordinated with the current logo (see attached). The webpage needs to be compatible with Wordpress to allow for easy changes to be made to the website for the user.
Required tabs for the page include:
- Civil Engineering
- Structural Engineering
- Project Management
- Business Management
- Project Controls
- Drafting
- Contact Us

Clean and efficient website that matches the services provided by the business.

Target Market(s)

New Customers to a very competitive market

Industry/Entity Type

Engineering

Number of Pages Required

5+ page

Requirements
Must have
• Clean with large stock photos

```html
<!DOCTYPE html>
<html lang="en">
<head>
<meta charset="utf-8">
<title>Talvero Engineering &amp; Management Services</title>
<link href="https://fonts.googleapis.com/css2?family=Oswald:wght@300;400;500&family=Open+Sans:wght@400;600;700&display=swap" rel="stylesheet">
<style>
:root{
  --orange:#f26522;
  --orange-dark:#d9541a;
  --ink:#333333;
  --muted:#8a8a8a;
  --light:#f3f3f3;
  --line:#e2e2e2;
  --footer:#2b2b2b;
  --footer-deep:#1f1f1f;
  --white:#ffffff;
}
*{box-sizing:border-box;margin:0;padding:0}
html,body{width:1200px;height:2288px;overflow:hidden}
body{position:relative;background:var(--white);font-family:"Open Sans",Arial,sans-serif;color:var(--ink);font-size:13px}
.abs{position:absolute}
.heading{font-family:"Oswald",Arial,sans-serif;font-weight:300;text-transform:uppercase;letter-spacing:1px}
.accent{color:var(--orange)}

/* top bar */
.topbar{top:0;left:0;width:1200px;height:48px;background:var(--white);border-bottom:1px solid var(--line);font-size:12px;color:var(--muted)}
.topbar .contact{top:16px;display:flex;align-items:center;gap:8px}
.topbar .social{top:14px;right:80px;display:flex;gap:10px}
.dot{width:20px;height:20px;border-radius:50%;background:#c8c8c8}

/* nav */
.nav{top:48px;left:0;width:1200px;height:64px;background:var(--white)}
.brand{left:80px;top:14px;display:flex;align-items:center;gap:10px}
.brand .mark{width:36px;height:36px;border-radius:50%;background:var(--orange)}
.brand .name{font-family:"Oswald",sans-serif;font-weight:500;font-size:22px;color:var(--orange);line-height:1}
.brand small{display:block;font-family:"Open Sans",sans-serif;font-size:9px;color:var(--ink);letter-spacing:1px;margin-top:3px;font-weight:600}
.menu{right:80px;top:0;display:flex;height:64px}
.menu a{display:block;padding:0 26px;line-height:64px;font-size:12px;color:var(--ink);text-decoration:none;font-weight:600;letter-spacing:.5px}
.menu a.active{color:var(--white);background:var(--orange)}

/* hero */
.hero{top:112px;left:0;width:1200px;height:480px;background:linear-gradient(160deg,#6b7a88 0%,#a9b6c2 45%,#d7dde3 70%,#8d99a4 100%)}
.hero .shade{inset:0;background:linear-gradient(90deg,rgba(0,0,0,.35),rgba(0,0,0,.05) 60%,rgba(0,0,0,.2))}
.hero-title{top:250px;width:1200px;text-align:center;color:var(--white);font-family:"Oswald",sans-serif;font-size:42px;font-weight:400}
.hero-sub{top:310px;width:1200px;text-align:center;color:var(--white);font-size:13px;line-height:19px}
.btn{display:inline-block;background:var(--orange);color:var(--white);font-size:11px;font-weight:700;letter-spacing:1px;text-transform:uppercase}
.hero .btn{top:362px;left:550px;width:100px;height:30px;line-height:30px;text-align:center}

/* services */
.services{top:592px;left:0;width:1200px;height:416px;background:var(--white)}
.section-title{width:1200px;text-align:center;font-size:34px;color:var(--ink)}
.services .section-title{top:38px}
.rule{height:2px;background:var(--orange);width:60px;left:570px}
.arrow{width:30px;height:30px;top:160px}
.service{top:110px;width:200px;text-align:center}
.service .ring{width:104px;height:104px;margin:0 auto;border-radius:50%;border:3px solid var(--orange);display:flex;align-items:center;justify-content:center}
.service .ring.filled{background:var(--orange)}
.service h3{font-family:"Oswald",sans-serif;font-weight:400;font-size:17px;text-transform:uppercase;margin-top:20px;line-height:20px;height:42px}
.service p{font-size:11px;color:var(--muted);line-height:16px;margin-top:6px;padding:0 20px}
.service .more{display:inline-block;margin-top:14px;border:1px solid var(--orange);color:var(--orange);font-size:10px;padding:3px 14px}

/* about */
.about{top:1008px;left:0;width:1200px;height:372px;background:var(--light)}
.about .badge{top:-32px;left:568px;width:64px;height:64px;border-radius:50%;background:var(--orange);border:5px solid var(--white)}
.about-title{left:140px;top:104px;font-size:32px;color:#555}
.about-title span{font-size:13px;color:var(--orange);font-family:"Open Sans",sans-serif;font-weight:600;letter-spacing:.5px;margin-left:6px}
.about-text{left:140px;top:160px;width:620px;font-size:11.5px;line-height:18px;color:var(--muted)}
.pillar{top:268px;display:flex;gap:12px;width:220px}
.pillar .icon{flex:none;width:46px;height:46px;border-radius:50%;border:2px solid var(--orange)}
.pillar h4{font-family:"Oswald",sans-serif;font-weight:400;font-size:15px}
.pillar p{font-size:10.5px;color:var(--muted);line-height:15px;margin-top:3px}
.consult{left:780px;top:84px;width:352px;height:288px;background:var(--white);box-shadow:0 0 0 1px var(--line)}
.consult .tab{top:-14px;left:0;width:352px;height:40px;background:var(--orange);color:var(--white);text-align:center;line-height:40px;font-family:"Oswald",sans-serif;font-size:18px;letter-spacing:1px}
.field{left:24px;width:160px;height:26px;border:1px solid var(--line);font-size:10px;color:var(--muted);padding:6px 8px;background:var(--white)}
.consult .btn{left:24px;top:236px;width:100px;height:30px;line-height:30px;text-align:center;font-size:12px}

/* testimonials */
.testimonials{top:1380px;left:0;width:1200px;height:420px;background:var(--orange);color:var(--white)}
.testimonials .section-title{top:34px;color:var(--white);font-size:32px}
.testimonials .rule{top:92px;background:var(--white)}
.quote-card{top:140px;width:360px;height:134px;background:var(--white);color:var(--muted);padding:18px 20px;font-size:10.5px;line-height:16px}
.quote-card .co{position:absolute;right:18px;bottom:12px;font-family:"Open Sans",sans-serif;font-weight:700;font-size:14px;color:var(--ink)}
.person{top:300px;display:flex;align-items:center;gap:12px}
.person .avatar{width:46px;height:46px;border-radius:50%;background:linear-gradient(#d9c7b8,#9a8577);border:2px solid var(--white)}
.person b{display:block;font-size:12px}
.person span{font-size:10px;opacity:.85}
.pager{top:400px;left:580px;width:40px;height:40px;border-radius:50%;background:var(--white);border:2px solid var(--line)}

/* clients */
.clients{top:1800px;left:0;width:1200px;height:148px;background:var(--white)}
.clients-title{left:50px;top:50px;font-size:26px;line-height:28px;color:var(--ink)}
.client{top:46px;width:140px;height:56px;border:1px solid var(--line);display:flex;align-items:center;justify-content:center;gap:8px;font-family:"Open Sans",sans-serif;font-weight:700;font-size:15px;color:#555}
.client i{width:12px;height:12px;background:#555;display:block}

/* newsletter */
.newsletter{top:1948px;left:0;width:1200px;height:52px;background:var(--orange)}
.newsletter .label{left:180px;top:14px;color:var(--white);font-family:"Oswald",sans-serif;font-size:19px;letter-spacing:1px}
.newsletter .input{left:600px;top:12px;width:260px;height:28px;background:var(--white);font-size:10px;color:var(--muted);padding:7px 10px}
.newsletter .go{left:880px;top:12px;width:120px;height:28px;background:#111;color:var(--white);font-size:11px;text-align:center;line-height:28px}

/* footer */
.footer{top:2000px;left:0;width:1200px;height:260px;background:var(--footer);color:#bdbdbd}
.footer h5{font-family:"Oswald",sans-serif;font-weight:400;font-size:16px;color:var(--white);border-bottom:1px solid #444;padding-bottom:8px;margin-bottom:12px}
.footer ul{list-style:none;font-size:11px;line-height:26px}
.footer li::before{content:"›";color:var(--orange);margin-right:8px}
.crow{display:flex;gap:10px;font-size:11px;line-height:16px;margin-bottom:12px}
.crow svg{flex:none}
.map{left:580px;top:34px;width:240px;height:170px;background:linear-gradient(135deg,#e6e3dc,#cfd6d0)}
.follow{display:flex;align-items:center;gap:10px;margin-bottom:10px;font-size:11px}
.follow .dot{background:var(--orange);width:26px;height:26px}
.follow b{display:block;color:var(--white);font-weight:600}
.follow span{font-size:9px}
.copyright{top:2260px;left:0;width:1200px;height:28px;background:var(--footer-deep);color:#8a8a8a;font-size:9.5px;line-height:28px}
</style>
</head>
<body>

<header class="abs topbar">
  <div class="abs contact" style="left:160px">
    <svg width="14" height="14" viewBox="0 0 24 24"><path fill="#f26522" d="M6.6 10.8a15 15 0 0 0 6.6 6.6l2.2-2.2c.3-.3.7-.4 1-.2 1.1.4 2.3.6 3.6.6.6 0 1 .4 1 1V20c0 .6-.4 1-1 1A17 17 0 0 1 3 4c0-.6.4-1 1-1h3.5c.6 0 1 .4 1 1 0 1.3.2 2.5.6 3.6.1.3 0 .7-.2 1z"/></svg>
    (02) 5550 0148
  </div>
  <div class="abs contact" style="left:340px">
    <svg width="14" height="14" viewBox="0 0 24 24"><rect x="2" y="5" width="20" height="14" fill="#f26522"/><path d="M2 5l10 8 10-8" fill="none" stroke="#fff" stroke-width="1.6"/></svg>
    info@talvero.com
  </div>
  <div class="abs social"><span class="dot"></span><span class="dot"></span><span class="dot"></span><span class="dot"></span><span class="dot"></span></div>
</header>

<nav class="abs nav">
  <div class="abs brand">
    <span class="mark"></span>
    <div class="name">TALVERO<small>ENGINEERING &amp; MANAGEMENT SERVICES</small></div>
  </div>
  <div class="abs menu">
    <a class="active" href="#">HOME</a><a href="#">ABOUT US</a><a href="#">OUR SERVICE</a><a href="#">CONTACT US</a>
  </div>
</nav>

<section class="abs hero" role="img" aria-label="Photo of two engineers in hard hats looking over a city skyline">
  <div class="abs shade"></div>
  <h1 class="abs hero-title">Lorem ipsum dolor sit</h1>
  <p class="abs hero-sub">Lorem ipsum dolor sit amet, consectetur adipiscing elit, sed diam<br>nonummy nibh euismod tincidunt ut laoreet dolore.</p>
  <a class="abs btn">Read more</a>
</section>

<section class="abs services">
  <h2 class="abs section-title heading">Our Business <span class="accent" style="font-weight:400">Services</span></h2>
  <div class="abs rule" style="top:96px"></div>
  <svg class="abs arrow" style="left:40px" viewBox="0 0 30 30"><path d="M19 7l-8 8 8 8" fill="none" stroke="#999" stroke-width="2.5"/></svg>
  <svg class="abs arrow" style="left:1130px" viewBox="0 0 30 30"><path d="M11 7l8 8-8 8" fill="none" stroke="#999" stroke-width="2.5"/></svg>

  <div class="abs service" style="left:100px">
    <div class="ring filled"><svg width="52" height="52" viewBox="0 0 52 52"><path d="M10 34a16 16 0 0 1 32 0z" fill="#fff"/><rect x="6" y="34" width="40" height="5" fill="#fff"/><rect x="24" y="14" width="4" height="10" fill="#f26522"/></svg></div>
    <h3>Civil<br>Engineering</h3>
    <p>Lorem ipsum dolor sit amet consectetur adipiscing elit sed diam.</p>
    <span class="more">Read more</span>
  </div>
  <div class="abs service" style="left:300px">
    <div class="ring"><svg width="52" height="52" viewBox="0 0 52 52"><rect x="6" y="18" width="6" height="16" fill="#f26522"/><rect x="40" y="18" width="6" height="16" fill="#f26522"/><rect x="12" y="24" width="28" height="4" fill="#f26522"/></svg></div>
    <h3>Structural<br>Engineering</h3>
    <p>Lorem ipsum dolor sit amet consectetur adipiscing elit sed diam.</p>
    <span class="more">Read more</span>
  </div>
  <div class="abs service" style="left:500px">
    <div class="ring"><svg width="52" height="52" viewBox="0 0 52 52"><rect x="13" y="10" width="26" height="34" fill="none" stroke="#f26522" stroke-width="3"/><path d="M18 22h16M18 29h16M18 36h10" stroke="#f26522" stroke-width="3"/></svg></div>
    <h3>Project<br>Management</h3>
    <p>Lorem ipsum dolor sit amet consectetur adipiscing elit sed diam.</p>
    <span class="more">Read more</span>
  </div>
  <div class="abs service" style="left:700px">
    <div class="ring"><svg width="52" height="52" viewBox="0 0 52 52"><circle cx="26" cy="18" r="8" fill="#f26522"/><path d="M12 42a14 14 0 0 1 28 0z" fill="#f26522"/></svg></div>
    <h3>Business<br>Management</h3>
    <p>Lorem ipsum dolor sit amet consectetur adipiscing elit sed diam.</p>
    <span class="more">Read more</span>
  </div>
  <div class="abs service" style="left:900px">
    <div class="ring"><svg width="52" height="52" viewBox="0 0 52 52"><path d="M8 36a18 18 0 0 1 36 0" fill="none" stroke="#f26522" stroke-width="3"/><path d="M26 36l9-12" stroke="#f26522" stroke-width="3"/><circle cx="26" cy="36" r="3" fill="#f26522"/></svg></div>
    <h3>Project<br>Controls</h3>
    <p>Lorem ipsum dolor sit amet consectetur adipiscing elit sed diam.</p>
    <span class="more">Read more</span>
  </div>
</section>

<section class="abs about">
  <span class="abs badge"></span>
  <h2 class="abs about-title heading">About Talvero <span>ENGINEERING &amp; MANAGEMENT SERVICES</span></h2>
  <p class="abs about-text">Lorem ipsum dolor sit amet, consectetur adipiscing elit, sed diam nonummy nibh euismod tincidunt ut laoreet dolore magna aliquam erat volutpat. Ut wisi enim ad minim veniam, quis nostrud exerci tation ullamcorper suscipit lobortis nisl ut aliquip ex ea commodo consequat. Duis autem vel eum iriure dolor in hendrerit in vulputate velit esse molestie consequat, vel illum dolore eu feugiat nulla facilisis.</p>
  <div class="abs pillar" style="left:200px"><span class="icon"></span><div><h4>Who We Are</h4><p>Lorem ipsum dolor sit amet consectetur elit sed diam nonummy.</p></div></div>
  <div class="abs pillar" style="left:460px"><span class="icon"></span><div><h4>Our Vision</h4><p>Lorem ipsum dolor sit amet consectetur elit sed diam nonummy.</p></div></div>

  <form class="abs consult">
    <div class="abs tab">FREE CONSULTATION</div>
    <div class="abs field" style="top:46px">First Name *</div>
    <div class="abs field" style="top:82px">Last Name *</div>
    <div class="abs field" style="top:118px">Number Phone *</div>
    <div class="abs field" style="top:154px">Email *</div>
    <div class="abs field" style="top:46px;left:200px;width:128px;height:134px">Message</div>
    <div class="abs btn">SUBMIT</div>
  </form>
</section>

<section class="abs testimonials">
  <h2 class="abs section-title heading">What Our Customer Say About Us</h2>
  <div class="abs rule"></div>
  <div class="abs quote-card" style="left:232px">Lorem ipsum dolor sit amet, consectetuer adipiscing elit, sed diam nonummy nibh euismod tincidunt ut laoreet dolore magna aliquam erat volutpat ut wisi enim ad minim veniam.<span class="co">Halden Works</span></div>
  <div class="abs quote-card" style="left:608px">Lorem ipsum dolor sit amet, consectetuer adipiscing elit, sed diam nonummy nibh euismod tincidunt ut laoreet dolore magna aliquam erat volutpat ut wisi enim ad minim veniam.<span class="co">Orvik</span></div>
  <div class="abs person" style="left:260px"><span class="avatar" role="img" aria-label="Portrait of client"></span><div><b>Clara Dunmore</b><span>Project Director</span></div></div>
  <div class="abs person" style="left:636px"><span class="avatar" role="img" aria-label="Portrait of client"></span><div><b>Owen Ridley</b><span>Site Manager</span></div></div>
  <svg class="abs pager" viewBox="0 0 40 40"><path d="M14 17l6 6 6-6" fill="none" stroke="#f26522" stroke-width="2.5"/></svg>
</section>

<section class="abs clients">
  <h2 class="abs clients-title heading">Our<br><span class="accent" style="font-weight:400">Clients</span></h2>
  <div class="abs client" style="left:320px"><i></i>Halden Works</div>
  <div class="abs client" style="left:480px">Linea Studio</div>
  <div class="abs client" style="left:640px"><i></i>Orvik</div>
  <div class="abs client" style="left:800px">Tessel</div>
  <div class="abs client" style="left:960px">Brennan</div>
  <svg class="abs" style="left:1120px;top:60px" width="30" height="30" viewBox="0 0 30 30"><path d="M11 7l8 8-8 8" fill="none" stroke="#999" stroke-width="2.5"/></svg>
</section>

<section class="abs newsletter">
  <div class="abs label">SUBSCRIBE TO OUR NEWSLETTER</div>
  <div class="abs input">Enter your email address</div>
  <div class="abs go">Subscribe</div>
</section>

<footer class="abs footer">
  <div class="abs" style="left:140px;top:34px;width:170px">
    <h5>Quick Links</h5>
    <ul><li>Home</li><li>About Us</li><li>Services</li><li>Our Services</li><li>Contact</li></ul>
  </div>
  <div class="abs" style="left:340px;top:34px;width:210px">
    <h5>Contact us</h5>
    <div class="crow"><svg width="14" height="16" viewBox="0 0 24 28"><path d="M12 0a10 10 0 0 0-10 10c0 8 10 18 10 18s10-10 10-18A10 10 0 0 0 12 0z" fill="#f26522"/><circle cx="12" cy="10" r="4" fill="#2b2b2b"/></svg><span>TALVERO ENGINEERING &amp;<br>MANAGEMENT SERVICES<br>14 Harlow Street, Brindale</span></div>
    <div class="crow"><svg width="14" height="14" viewBox="0 0 24 24"><rect x="2" y="5" width="20" height="14" fill="#f26522"/></svg><span>info@talvero.com</span></div>
    <div class="crow"><svg width="14" height="14" viewBox="0 0 24 24"><circle cx="12" cy="12" r="10" fill="#f26522"/></svg><span>(02) 5550 0148</span></div>
  </div>
  <div class="abs map" role="img" aria-label="Street map showing office location"></div>
  <div class="abs" style="left:900px;top:34px;width:200px">
    <h5>Follow Us</h5>
    <div class="follow"><span class="dot"></span><div><b>Friendwall</b><span>Join us today</span></div></div>
    <div class="follow"><span class="dot"></span><div><b>Searchly</b><span>Join us today</span></div></div>
    <div class="follow"><span class="dot"></span><div><b>Chirper</b><span>Join us today</span></div></div>
    <div class="follow"><span class="dot"></span><div><b>Workring</b><span>Join us today</span></div></div>
  </div>
</footer>
<div class="abs copyright"><span style="margin-left:140px">© 2024 TALVERO ENGINEERING &amp; MANAGEMENT SERVICES</span><span style="float:right;margin-right:140px">ALL RIGHTS RESERVED</span></div>

</body>
</html>
```